Bar Soap Packaging Design for Facial Cleansing Bar

Hi,

I have a business that sells soaps, lotions, and other skincare products and I'd like a design for a box for a bar soap that is primarily for women.

The name of the brand is 'Velmo Shea Blend' and the brand is all about renewal and rejuvenation.

I've attached my logo and photos of packaging for bar soaps that are best sellers in my market.

The box is 3 inches x 2 inches and has a white background.

Info to go on the box:

1. Brand name: Velmo Shea Blend

2. [To go below brand name]: Facial Bar

3. Address: Distributed by Haverlin Trading Ltd, 47 Marlow St., Kingston, Jamaica W.I.

4. Contact: tamsin@velmosheablend.example

5. Net Weight: 3.6 oz /102g

6. Ingredients: glycerine, palmitic acid, sodium chloride, water, cocoa butter, fragrance, AOS, EDTA, vitamin E, color.

7. Directions: Wet face. Lather soap in hands. Gently massage lather onto face and neck. Rinse with water and pat dry with a towel. For day, follow with a sunscreen. At night, follow with a serum and/or moisturizer.

8. Please put a circle somewhere on the front with the words: 'Boosts Hydration 100%' in the circle

9. Batch Code: [please leave space beside 'Batch Code' blank]

10. Best Before: April 2019

11. Please put somewhere on the the front: For Younger Looking Skin

12. Please put somewhere on the front: with Real Cocoa Butter and Vitamin E

Thank you,
Tamsin

Target Market(s)

Women 27 to 60 who are looking for anti-age skincare products that'll make them look younger

Industry/Entity Type

Business

Font styles to use
Sans Serif

Colors

Designer to choose colors to be used in the design.

Requirements
Must have
• The info that I've asked for in the brief
Nice to have
• A design similar to the packaging for the brand of soap 'Odra' that I've attached.
Should not have
• Not sure...

```html
<!DOCTYPE html>
<html lang="en">
<head>
<meta charset="utf-8">
<title>Velmo Shea Blend – Facial Bar Box</title>
<link href="https://fonts.googleapis.com/css2?family=Marcellus&family=Arimo:wght@400;700&family=Great+Vibes&display=swap" rel="stylesheet">
<style>
  :root {
    --brand-blue: #1a73c4;
    --sky-blue: #1ea8e6;
    --navy: #1b4f94;
    --panel-blue: #c9dceb;
    --panel-grey: #c4c4c4;
    --band-blue: #b5cfe2;
    --frame-purple: #8a4a9c;
    --ink: #1f1f1f;
    --maroon: #5a1010;
    --orange: #f28a0c;
    --peach: #fbcf94;
    --white: #ffffff;
  }
  * { margin: 0; padding: 0; box-sizing: border-box; }
  html, body { width: 1200px; height: 881px; overflow: hidden; background: var(--white); }
  .box-flat { position: relative; width: 1200px; height: 881px; background: var(--white); overflow: hidden; font-family: "Arimo", sans-serif; }

  /* side panel */
  .side-panel { position: absolute; left: 0; top: 0; width: 248px; height: 634px;
    background: linear-gradient(90deg, var(--white) 0%, var(--panel-blue) 100%); }
  .side-panel-base { position: absolute; left: 0; top: 634px; width: 248px; height: 247px; background: var(--panel-grey);
    padding: 16px 14px; color: var(--ink); }
  .directions { font-size: 12px; line-height: 16px; }
  .directions strong { font-weight: 700; }
  .batch-code { margin-top: 10px; font-size: 12px; font-weight: 700; display: flex; align-items: flex-end; gap: 6px; }
  .batch-code .blank { flex: 1; border-bottom: 1px solid var(--ink); height: 12px; }
  .side-name { position: absolute; left: 98px; top: 78px; writing-mode: vertical-rl;
    font-family: "Marcellus", serif; font-size: 104px; line-height: 1; color: var(--brand-blue); }
  .side-label { position: absolute; left: 21px; top: 111px; width: 47px; height: 285px;
    border: 3px solid var(--frame-purple); border-radius: 6px; background: var(--white);
    writing-mode: vertical-rl; display: flex; align-items: center; justify-content: center;
    font-family: "Marcellus", serif; font-size: 26px; color: var(--ink); letter-spacing: 1px; }

  /* badges */
  .hydration-badge { position: absolute; border: 4px solid var(--navy); border-radius: 50%;
    background: var(--white); display: flex; flex-direction: column; align-items: center; justify-content: center;
    font-family: "Arimo", sans-serif; font-weight: 700; color: var(--navy); line-height: 1.15; text-align: center; }
  .badge-top { left: 1038px; top: 35px; width: 110px; height: 110px; font-size: 15px; transform: rotate(22deg); }
  .badge-side { left: 110px; top: 473px; width: 96px; height: 96px; font-size: 12px; transform: rotate(90deg); }
  .badge-band { left: 594px; top: 730px; width: 100px; height: 100px; font-size: 13px; }

  /* imagery */
  .butter-chunks { position: absolute; left: 180px; top: 0; width: 410px; height: 350px;
    background: radial-gradient(ellipse at 50% 45%, #f1dcae 0%, #e8cf9c 45%, rgba(255,255,255,0) 75%); }
  .cacao-pods { position: absolute; left: 250px; top: 330px; width: 490px; height: 304px;
    background: radial-gradient(ellipse at 48% 55%, #6a3a2c 0%, #7e4a36 40%, #8b5a40 58%, rgba(255,255,255,0) 76%); }

  /* main front */
  .brand-name { position: absolute; left: 430px; top: 10px; width: 600px; text-align: center;
    font-family: "Marcellus", serif; font-size: 160px; line-height: 1; color: var(--brand-blue); }
  .product-label { position: absolute; left: 652px; top: 264px; width: 415px; height: 72px;
    border: 3px solid var(--frame-purple); border-radius: 8px; display: flex; align-items: center; justify-content: center;
    font-family: "Marcellus", serif; font-size: 42px; color: var(--ink); letter-spacing: 1px; }
  .product-subtitle { position: absolute; left: 652px; top: 352px; width: 415px; text-align: center;
    font-family: "Marcellus", serif; font-size: 30px; letter-spacing: 3px; color: var(--frame-purple); }
  .feature-pill { position: absolute; left: 718px; top: 435px; width: 386px; height: 77px; border-radius: 8px;
    background: linear-gradient(90deg, var(--peach) 0%, #fde0b6 100%);
    display: flex; flex-direction: column; align-items: center; justify-content: center; font-weight: 700; line-height: 1.2; }
  .feature-pill .line-one { font-size: 22px; color: var(--maroon); }
  .feature-pill .line-two { font-size: 27px; color: var(--orange); }
  .tagline { position: absolute; left: 752px; top: 540px; font-family: "Great Vibes", cursive;
    font-size: 46px; font-weight: 700; color: var(--sky-blue); white-space: nowrap; }

  /* info band */
  .info-band { position: absolute; left: 248px; top: 634px; width: 952px; height: 247px;
    background: linear-gradient(180deg, var(--band-blue) 0%, var(--white) 70%); }
  .band-name { position: absolute; left: 280px; top: 678px; font-family: "Marcellus", serif;
    font-size: 96px; line-height: 1; color: var(--brand-blue); }
  .band-label { position: absolute; left: 282px; top: 816px; width: 266px; height: 45px;
    border: 3px solid var(--frame-purple); border-radius: 6px; display: flex; align-items: center; justify-content: center;
    font-family: "Marcellus", serif; font-size: 27px; color: var(--ink); letter-spacing: 1px; }
  .product-details { position: absolute; left: 724px; top: 662px; width: 445px; font-size: 16px; line-height: 23px; color: var(--ink); }
  .product-details .best-before { font-size: 15px; }
  .net-weight { position: absolute; left: 722px; top: 828px; font-size: 31px; color: #000; white-space: nowrap; }
</style>
</head>
<body>
<main class="box-flat">
  <section class="side-panel" aria-label="Side panel">
    <div class="side-label">SHEA BLEND</div>
    <div class="side-name">Velmo</div>
  </section>
  <section class="side-panel-base" aria-label="Directions and batch code">
    <p class="directions"><strong>Directions:</strong> Wet face. Lather soap in hands. Gently massage lather onto face and neck. Rinse with water and pat dry with a towel. For day, follow with a sunscreen. At night, follow with a serum and/or moisturizer.</p>
    <p class="batch-code">Batch Code: <span class="blank"></span></p>
  </section>
  <div class="hydration-badge badge-side"><span>BOOSTS</span><span>HYDRATION</span><span>100%</span></div>

  <div class="butter-chunks" role="img" aria-label="Photo of broken chunks of raw butter"></div>
  <div class="cacao-pods" role="img" aria-label="Photo of opened cacao pods with beans and green leaves"></div>

  <h1 class="brand-name">Velmo</h1>
  <div class="product-label">SHEA BLEND</div>
  <p class="product-subtitle">FACIAL BAR</p>
  <div class="hydration-badge badge-top"><span>BOOSTS</span><span>HYDRATION</span><span>100%</span></div>

  <div class="feature-pill">
    <span class="line-one">with Real Cocoa Butter</span>
    <span class="line-two">&amp; Vitamin E</span>
  </div>
  <p class="tagline">For Younger Looking Skin</p>

  <section class="info-band" aria-label="Product information"></section>
  <div class="band-name">Velmo</div>
  <div class="band-label">SHEA BLEND</div>
  <div class="hydration-badge badge-band"><span>BOOSTS</span><span>HYDRATION</span><span>100%</span></div>

  <div class="product-details">
    <p>Ingredients: glycerine, palmitic acid, sodium chloride, water, cocoa butter, fragrance, AOS, EDTA, vitamin E, color.</p>
    <p>Distributed by</p>
    <p>Haverlin Trading Ltd, 47 Marlow St.,</p>
    <p>Kingston, Jamaica W.I.</p>
    <p>Mail: tamsin@velmosheablend.example</p>
    <p class="best-before">Best Before: April 2019</p>
  </div>
  <p class="net-weight">Net Weight: 3.6 oz /102g</p>
</main>
</body>
</html>
```